WP website design (Bluefinch)

We need a wordpress design for an established auction and real estate company based in Arkansas. The winning design will incorporate a professional color scheme with company logo in a clean layout. The design needs to consider that this will be developed on a responsive theme.

Industry/Entity Type

Real Estate

Font styles to use
Sans Serif

Colors

Designer to choose colors to be used in the design.

Requirements
Must have
• Site will have slideshow, please use stock real estate or other image. A rough idea of homepage content is attached - not necessarily for design purposes.

Navigation Structure is:
1) Home
2) Auctions
3) Services
4) For Sale
5) About Us
6) Rex Videos
7) News & Events
8) Contact Us

Widgets will include:
Social media icons (Facebook, Youtube, RSS)
Testimonials Widget - this should be prominent
Featured Video
Email Signup form (Sign up to receive exclusive email updates for Bluefinch auctions. )
Nice to have
• A drop down menu example
Should not have
• no gavel in the design

```html
<!DOCTYPE html>
<html lang="en">
<head>
<meta charset="utf-8">
<title>Bluefinch Auction &amp; Marketing</title>
<link href="https://fonts.googleapis.com/css2?family=Source+Sans+3:ital,wght@0,400;0,600;0,700;1,400&family=PT+Sans+Narrow:wght@400;700&display=swap" rel="stylesheet">
<style>
:root{
  --green:#1a8a2e;
  --green-dark:#0f6b21;
  --ink:#222;
  --text:#555;
  --muted:#777;
  --panel:#efefef;
  --panel-head:#d6d6d6;
  --nav:#1b1b1b;
  --footer:#161616;
  --line:#ddd;
}
*{box-sizing:border-box;margin:0;padding:0}
html,body{width:856px;height:1200px;overflow:hidden;background:#fff}
body{position:relative;font-family:"Source Sans 3",sans-serif;color:var(--text)}
.abs{position:absolute}

.brand{left:62px;top:34px;font-size:34px;font-weight:700;color:var(--ink);letter-spacing:.5px;display:flex;align-items:center;gap:8px}
.brand-dot{width:14px;height:14px;border-radius:50%;background:var(--green)}
.search{left:608px;top:43px;width:186px;height:25px;border:1px solid #ccc;font-size:11px;color:#888;padding:5px 8px;display:flex;justify-content:space-between;align-items:center}

.nav{left:62px;top:100px;width:732px;height:39px;background:var(--nav);display:flex;border-radius:2px}
.nav a{color:#fff;text-decoration:none;font-size:13px;display:flex;align-items:center;justify-content:center;border-right:1px solid #3a3a3a;height:100%}
.nav a:last-child{border-right:none}

.tagline{left:0;width:856px;top:158px;text-align:center;color:var(--green);font-size:23px;font-weight:400}

.slide{left:62px;top:206px;width:501px;height:243px;background:linear-gradient(90deg,#ececec,#f7f7f5 60%,#e6e6e6)}
.slide-caption{left:92px;top:410px;font-family:"PT Sans Narrow",sans-serif;font-weight:700;font-size:25px;color:#444}
.dots{left:481px;top:425px;display:flex;gap:5px}
.dots span{width:12px;height:12px;border-radius:50%;background:#ddd}
.dots span:first-child{background:#aaa}

.agent{left:581px;top:206px;width:213px;height:243px;background:linear-gradient(180deg,#7ea8b3,#3f5f66)}
.agent-cap{left:581px;top:398px;width:213px;height:51px;background:linear-gradient(180deg,var(--green),var(--green-dark));color:#fff;font-family:"PT Sans Narrow",sans-serif;font-size:13px;line-height:22px;padding:4px 16px}

.section-title{font-size:17px;color:#444}
.auctions-title{left:62px;top:489px}

.auction{left:62px;width:454px;height:184px;background:var(--panel)}
.auction-head{position:absolute;left:8px;top:11px;width:437px;height:35px;background:var(--panel-head);font-size:14px;color:#333;padding:8px 10px;letter-spacing:.3px}
.auction-img{position:absolute;left:10px;top:63px;width:138px;height:104px;border:2px solid #fff;box-shadow:0 0 0 1px #ddd}
.auction-body{position:absolute;left:168px;top:62px;width:282px}
.auction-body h3{font-size:13px;font-weight:400;color:var(--green);margin-bottom:6px}
.auction-body p{font-size:10.5px;line-height:18px;color:#666}
.auction-body p a{color:var(--green);text-decoration:none}
.auction-meta{position:absolute;left:170px;top:150px;display:flex;gap:34px;font-size:13px;color:#555}
.auction-meta span{display:flex;align-items:center;gap:10px}

.video{left:563px;top:527px;width:231px;height:136px;background:linear-gradient(180deg,#7b6b56,#4a3f33 70%,#2d2a27)}
.play{left:659px;top:574px}

.signup{left:562px;top:694px;width:232px;height:180px;background:var(--panel)}
.signup-head{position:absolute;left:0;top:0;width:232px;height:36px;background:linear-gradient(180deg,var(--green),var(--green-dark));color:#fff;font-size:14px;padding:8px 12px}
.field{position:absolute;left:12px;width:208px;height:31px;background:#fff;border:1px solid #ccc;font-size:11px;color:#777;padding:8px 10px}
.submit{position:absolute;left:161px;top:137px;width:59px;height:26px;background:linear-gradient(180deg,#4a4a4a,#1f1f1f);color:#fff;font-family:"PT Sans Narrow",sans-serif;font-size:14px;text-align:center;line-height:26px;border-radius:2px}

.testi-title{left:564px;top:898px}
.quote{left:563px;top:930px;width:231px;height:78px;background:var(--panel);padding:10px 14px 0 28px;font-style:italic;font-size:9px;line-height:17px;color:#555}
.quote-tail{left:714px;top:1007px}
.q-mark{position:absolute;font-size:18px;color:#bbb;font-style:normal}
.author-img{left:572px;top:1024px;width:60px;height:56px;background:linear-gradient(180deg,#e8e8e8,#9aa3ad)}
.author{left:662px;top:1038px;font-size:10px;font-weight:700;color:#222;line-height:23px}
.author span{display:flex;align-items:center;gap:8px}

.footer{left:0;top:1126px;width:856px;height:74px;background:var(--footer)}
.footer-links{left:62px;top:1143px;font-size:10px;color:#eee}
.copy{left:62px;top:1167px;font-size:10px;color:#ddd}
.social{left:664px;top:1150px;display:flex;gap:10px}
.social span{width:25px;height:25px;display:block}
</style>
</head>
<body>

<div class="abs brand"><span>Bluefinch</span><span class="brand-dot"></span></div>
<div class="abs search"><span>Search..</span>
  <svg width="10" height="10" viewBox="0 0 10 10"><circle cx="4" cy="4" r="3" fill="none" stroke="#999" stroke-width="1.4"/><line x1="6.2" y1="6.2" x2="9" y2="9" stroke="#999" stroke-width="1.4"/></svg>
</div>

<nav class="abs nav">
  <a style="width:82px">Home</a>
  <a style="width:89px">Auctions</a>
  <a style="width:82px">Services</a>
  <a style="width:82px">For Sale</a>
  <a style="width:88px">About Us</a>
  <a style="width:96px">Rex Videos</a>
  <a style="width:118px">News &amp; Events</a>
  <a style="width:95px">Contact Us</a>
</nav>

<div class="abs tagline">- Serving the Arkansas &amp; Oklahoma Regions -</div>

<div class="abs slide" role="img" aria-label="Smiling young man in a bright home office"></div>
<div class="abs slide-caption">DUIS AUTEM VEL EUM IRURE</div>
<div class="abs dots"><span></span><span></span><span></span><span></span></div>

<div class="abs agent" role="img" aria-label="Portrait of the auctioneer in front of a blue-green backdrop"></div>
<div class="abs agent-cap">REX HALVORNAM LIBER TEMPOR<br>LICENSE #1345</div>

<h2 class="abs section-title auctions-title">Current Auctions</h2>

<section class="abs auction" style="top:527px">
  <div class="auction-head">REAL ESTATE AUCTION</div>
  <div class="auction-img" role="img" aria-label="Model house on blueprints with a calculator" style="background:linear-gradient(135deg,#b9d2ea,#e9eef3 55%,#8aa7c4)"></div>
  <div class="auction-body">
    <h3>Nam liber tempor cum soluta nobis eleifend</h3>
    <p>Suspendisse eu erat quam. Vivamuis porttitinor eros quis ni si laciia sedm lorem vulputate. Aliquaom a orc quniis nisi sa gittis sagitti Dolor sitamet,consectetur adipis. <a>Read More</a></p>
  </div>
  <div class="auction-meta">
    <span><svg width="20" height="16" viewBox="0 0 20 16"><circle cx="7" cy="4" r="3.5" fill="#555"/><path d="M0 16c0-5 3-7 7-7s7 2 7 7z" fill="#555"/><circle cx="14" cy="3.5" r="2.8" fill="#888"/><path d="M13 8c4 0 7 2 7 7h-5c0-3-1-5-2-7z" fill="#888"/></svg>Dealers</span>
    <span><svg width="18" height="18" viewBox="0 0 18 18"><circle cx="9" cy="9" r="6" fill="none" stroke="#666" stroke-width="1.4" stroke-dasharray="2.4 1.4"/><circle cx="9" cy="9" r="3" fill="none" stroke="#666" stroke-width="1.4"/></svg>Claritas etiam</span>
  </div>
</section>

<section class="abs auction" style="top:714px">
  <div class="auction-head">REAL ESTATE AUCTION</div>
  <div class="auction-img" role="img" aria-label="Hand holding house keys in front of a brick home" style="background:linear-gradient(135deg,#5a3a2a,#b98d6c 55%,#7a4a32)"></div>
  <div class="auction-body">
    <h3>Nam liber tempor cum soluta nobis eleifend</h3>
    <p>Suspendisse eu erat quam. Vivamuis porttitinor eros quis ni si laciia sedm lorem vulputate. Aliquaom a orc quniis nisi sa gittis sagitti Dolor sitamet,consectetur adipis. <a>Read More</a></p>
  </div>
  <div class="auction-meta">
    <span><svg width="20" height="16" viewBox="0 0 20 16"><circle cx="7" cy="4" r="3.5" fill="#555"/><path d="M0 16c0-5 3-7 7-7s7 2 7 7z" fill="#555"/><circle cx="14" cy="3.5" r="2.8" fill="#888"/><path d="M13 8c4 0 7 2 7 7h-5c0-3-1-5-2-7z" fill="#888"/></svg>Dealers</span>
    <span><svg width="18" height="18" viewBox="0 0 18 18"><circle cx="9" cy="9" r="6" fill="none" stroke="#666" stroke-width="1.4" stroke-dasharray="2.4 1.4"/><circle cx="9" cy="9" r="3" fill="none" stroke="#666" stroke-width="1.4"/></svg>Claritas etiam</span>
  </div>
</section>

<section class="abs auction" style="top:900px">
  <div class="auction-head">REAL ESTATE AUCTION</div>
  <div class="auction-img" role="img" aria-label="Hands passing a set of keys" style="background:linear-gradient(135deg,#e3b59a,#f4e0d4 55%,#c98a6c)"></div>
  <div class="auction-body">
    <h3>Nam liber tempor cum soluta nobis eleifend</h3>
    <p>Suspendisse eu erat quam. Vivamuis porttitinor eros quis ni si laciia sedm lorem vulputate. Aliquaom a orc quniis nisi sa gittis sagitti Dolor sitamet,consectetur adipis. <a>Read More</a></p>
  </div>
  <div class="auction-meta">
    <span><svg width="20" height="16" viewBox="0 0 20 16"><circle cx="7" cy="4" r="3.5" fill="#555"/><path d="M0 16c0-5 3-7 7-7s7 2 7 7z" fill="#555"/><circle cx="14" cy="3.5" r="2.8" fill="#888"/><path d="M13 8c4 0 7 2 7 7h-5c0-3-1-5-2-7z" fill="#888"/></svg>Dealers</span>
    <span><svg width="18" height="18" viewBox="0 0 18 18"><circle cx="9" cy="9" r="6" fill="none" stroke="#666" stroke-width="1.4" stroke-dasharray="2.4 1.4"/><circle cx="9" cy="9" r="3" fill="none" stroke="#666" stroke-width="1.4"/></svg>Claritas etiam</span>
  </div>
</section>

<div class="abs video" role="img" aria-label="Featured video still of a brick storefront"></div>
<svg class="abs play" width="38" height="38" viewBox="0 0 38 38"><circle cx="19" cy="19" r="17" fill="rgba(255,255,255,.85)" stroke="#ccc" stroke-width="1.5"/><path d="M15 11l12 8-12 8z" fill="#aaa"/></svg>

<form class="abs signup">
  <div class="signup-head">Email Signup Form</div>
  <div class="field" style="top:53px">Email Id</div>
  <div class="field" style="top:94px">Password</div>
  <div class="submit">SUBMIT</div>
</form>

<h2 class="abs section-title testi-title">Testimonials</h2>
<blockquote class="abs quote">
  <span class="q-mark" style="left:14px;top:4px">&ldquo;</span>
  Fusce feugiat malesuada odio. Morbi nunc do gravida at, cursus nec, luctus a, lorem. Maecn as tristique orci acd sem. Lorem ipsum.
  <span class="q-mark" style="left:196px;top:48px">&rdquo;</span>
</blockquote>
<svg class="abs quote-tail" width="24" height="14" viewBox="0 0 24 14"><path d="M0 0h24L0 14z" fill="#efefef"/></svg>
<div class="abs author-img" role="img" aria-label="Portrait of the reviewer"></div>
<div class="abs author">
  <div>Maecenintty interu coquat</div>
  <span><svg width="11" height="11" viewBox="0 0 11 11"><circle cx="5.5" cy="3" r="2.6" fill="#333"/><path d="M0 11c0-4 2.5-5 5.5-5s5.5 1 5.5 5z" fill="#333"/></svg>Dana Morrow's</span>
</div>

<footer class="abs footer"></footer>
<div class="abs footer-links">Home | Auctions | Services | For Sale | About Us | Rex Videos | News &amp; Events | Contact Us</div>
<div class="abs copy">Copyrights 2013. All Rights Reserved.</div>
<div class="abs social">
  <span style="background:#3b5a9a" role="img" aria-label="Social link"></span>
  <span style="background:#2ba3e0" role="img" aria-label="Social link"></span>
  <span style="background:#f07b16" role="img" aria-label="Feed link"></span>
  <span style="background:#d62b2b" role="img" aria-label="Video channel link"></span>
</div>

</body>
</html>
```